Velmora EIRL Business Card Design Project

We need a business card design for a New Business Intelligence Consultant. We bring a complete service to the client from first consulting meeting to help desk and system improvement.

I will upload the company logo and I like to use the logo colors on the card. Feel free to use all logo components on the design, for example one side with the black logo using complete card and the other side only the red shape (is an example, feel absolutely free :)).

The principal idea is to sell a professional service and a modern company.

Target Market(s)

IT Business Intelligence Clients

Industry/Entity Type

Professional Service

Requirements
Nice to have
• - Use the logo colors and minimize white sections.
- Rounded borders
Should not have
• I don't want to see any references to people working on a meeting or office photos or any computers related logos.

```html
<!DOCTYPE html>
<html lang="es">
<head>
<meta charset="utf-8">
<title>Velmora EIRL – Tarjeta de presentación</title>
<link rel="stylesheet" href="https://fonts.googleapis.com/css2?family=Ubuntu:wght@300;400&display=swap">
<style>
  :root {
    --page: #ffffff;
    --card: #0a0b0b;
    --white: #f2f2f2;
    --soft: #d6d6d6;
    --red: #e41e1e;
    --brand-grey: #c9c9c9;
  }
  * { margin: 0; padding: 0; box-sizing: border-box; }
  html, body {
    width: 1200px; height: 400px; overflow: hidden;
    background: var(--page);
    font-family: "Ubuntu", sans-serif;
  }
  .stage { position: relative; width: 1200px; height: 400px; }
  .card {
    position: absolute; top: 27px;
    width: 566px; height: 346px;
    background: var(--card);
    border-radius: 46px;
  }
  .card--front { left: 25px; }
  .card--back  { left: 610px; }

  /* front */
  .brand {
    position: absolute; left: 173px; top: 154px;
    display: flex; align-items: center; gap: 16px;
  }
  .brand__mark { width: 30px; height: 30px; background: var(--red); }
  .brand__name {
    font-weight: 400; font-size: 42px; line-height: 1;
    color: var(--brand-grey); letter-spacing: 0.5px;
  }

  /* back */
  .holder {
    position: absolute; right: 100px; top: 116px; text-align: right;
  }
  .holder__name { font-size: 13px; font-weight: 400; color: var(--white); line-height: 15px; }
  .holder__role { font-size: 10px; font-weight: 300; color: var(--red); line-height: 12px; }

  .contact {
    position: absolute; right: 90px; top: 228px;
    display: grid; grid-template-columns: auto 16px;
    font-size: 8.5px; line-height: 11px; font-weight: 300;
  }
  .contact__value { color: var(--soft); text-align: right; }
  .contact__key { color: var(--red); text-align: right; }

  .website {
    position: absolute; right: 100px; top: 303px;
    font-size: 8.5px; font-weight: 300; color: var(--soft);
  }
</style>
</head>
<body>
<main class="stage">
  <section class="card card--front" aria-label="Anverso">
    <div class="brand">
      <span class="brand__mark"></span>
      <span class="brand__name">velmora</span>
    </div>
  </section>

  <section class="card card--back" aria-label="Reverso">
    <div class="holder">
      <p class="holder__name">Tomás Aldunate R.</p>
      <p class="holder__role">Gerente General</p>
    </div>
    <div class="contact">
      <span class="contact__value">+56 (9) 91234567</span><span class="contact__key">p</span>
      <span class="contact__value">tomas@velmora.cl</span><span class="contact__key">e</span>
      <span class="contact__value">Av. Los Almendros Sur 415</span><span class="contact__key">a</span>
      <span class="contact__value">Of.308. Providencia, Santiago</span><span class="contact__key"></span>
    </div>
    <p class="website">www.velmora.com</p>
  </section>
</main>
</body>
</html>
```